Marlow Crest Group (Real Estate and Investment)

A high end, clean design.
We are a real estate company with sales, asset management and investment divisions. We want to use a black and white scheme which is really high end feel. The back of the card can just be the logo (black background with the white writing) as we will probably emboss this when we print)

Target Market(s)

High level investors, high end houses for sale

Industry/Entity Type

Business

Contact Information for Business Card

Name, position, phone number and email address
Glen Varley, Managing Director, 0437259064 and glen@marlowcrest-example.com.au

Requirements
Must have
• Back of the card to be the black background with the white writing (as per the attached images). Would like the capacity to emboss the writing and logo

```html
<!DOCTYPE html>
<html lang="en">
<head>
<meta charset="utf-8">
<title>Marlow Crest Group – Business Card</title>
<link href="https://fonts.googleapis.com/css2?family=Open+Sans:wght@400&display=swap" rel="stylesheet">
<style>
  :root {
    --backdrop: #8f8f8f;
    --ink: #000000;
    --paper: #ffffff;
    --slate: #5f5f5f;
    --text-dark: #3a3a3a;
  }
  html, body {
    margin: 0;
    padding: 0;
    width: 980px;
    height: 1200px;
    overflow: hidden;
    background: var(--backdrop);
    font-family: "Open Sans", sans-serif;
  }
  .canvas {
    position: relative;
    width: 980px;
    height: 1200px;
  }
  .card {
    position: absolute;
    overflow: hidden;
  }
  .card-front {
    left: 117px;
    top: 130px;
    width: 725px;
    height: 410px;
    background: var(--ink);
  }
  .front-mark {
    position: absolute;
    left: 302px;
    top: 106px;
    width: 120px;
    height: 120px;
    box-sizing: border-box;
    border: 2px solid var(--paper);
    border-radius: 50%;
  }
  .front-name {
    position: absolute;
    left: 0;
    right: 0;
    top: 282px;
    text-align: center;
    color: var(--paper);
    font-size: 38px;
    font-weight: 400;
    letter-spacing: 0.5px;
    line-height: 1;
  }
  .card-back {
    left: 117px;
    top: 709px;
    width: 717px;
    height: 413px;
    background: var(--paper);
  }
  .back-shapes {
    position: absolute;
    inset: 0;
  }
  .holder-name {
    position: absolute;
    left: 43px;
    top: 24px;
    margin: 0;
    color: var(--text-dark);
    font-size: 29px;
    font-weight: 400;
    line-height: 1.2;
  }
  .holder-role {
    position: absolute;
    left: 24px;
    top: 66px;
    margin: 0;
    color: var(--text-dark);
    font-size: 21px;
    line-height: 1.2;
  }
  .back-mark {
    position: absolute;
    left: 69px;
    top: 291px;
    width: 68px;
    height: 68px;
    box-sizing: border-box;
    border: 1.5px solid var(--paper);
    border-radius: 50%;
  }
  .back-name {
    position: absolute;
    left: 10px;
    width: 186px;
    top: 370px;
    text-align: center;
    color: var(--paper);
    font-size: 15px;
    line-height: 1;
    letter-spacing: 0.3px;
  }
  .contact {
    position: absolute;
    left: 339px;
    display: flex;
    align-items: center;
    color: var(--paper);
  }
  .contact svg {
    flex: none;
    width: 38px;
    height: 36px;
    margin-right: 13px;
  }
  .contact-phone { top: 298px; font-size: 22px; }
  .contact-email { top: 358px; font-size: 19px; }
</style>
</head>
<body>
<main class="canvas">

  <section class="card card-front" aria-label="Card front">
    <div class="front-mark"></div>
    <div class="front-name">MARLOW CREST GROUP</div>
  </section>

  <section class="card card-back" aria-label="Card back">
    <svg class="back-shapes" width="717" height="413" viewBox="0 0 717 413" aria-hidden="true">
      <polygon points="717,0 717,413 322,413 215,324" fill="var(--slate)"/>
      <polygon points="0,146 322,413 0,413" fill="var(--ink)"/>
    </svg>

    <h1 class="holder-name">Glen Varley</h1>
    <p class="holder-role">Managing Director</p>

    <div class="back-mark"></div>
    <div class="back-name">MARLOW CREST GROUP</div>

    <div class="contact contact-phone">
      <svg viewBox="0 0 24 24" aria-hidden="true">
        <path fill="#ffffff" d="M6.6 3.2c.5-.4 1.2-.3 1.6.2l2.1 2.9c.4.5.3 1.2-.1 1.6l-1.4 1.3c.9 1.9 2.5 3.6 4.4 4.6l1.3-1.4c.4-.4 1.1-.5 1.6-.1l2.9 2.1c.5.4.6 1.1.2 1.6l-1.2 1.6c-.6.8-1.7 1.2-2.7.9C9.9 17.4 6.4 13.9 5.3 8.5c-.2-1 .1-2 .9-2.7z"/>
      </svg>
      <span>0437259064</span>
    </div>

    <div class="contact contact-email">
      <svg viewBox="0 0 40 38" aria-hidden="true">
        <g fill="none" stroke="#ffffff" stroke-width="1.8" stroke-linejoin="round">
          <polyline points="2,15 20,2 38,15"/>
          <rect x="2" y="15" width="36" height="21"/>
          <polyline points="2,15 20,27 38,15"/>
          <line x1="2" y1="36" x2="15" y2="24"/>
          <line x1="38" y1="36" x2="25" y2="24"/>
          <circle cx="20" cy="12" r="3.2"/>
        </g>
      </svg>
      <span>glen@marlowcrest-example.com.au</span>
    </div>
  </section>

</main>
</body>
</html>
```